WP website design for Brenwick

We need a wordpress design for an auction company. The winning design will incorporate a professional color scheme with company logo in a clean, image driven layout. The design needs to consider that this will be developed on a responsive theme. Colors are those that will highlight the logo.

Industry/Entity Type

It Company

Font styles to use
Serif
Sans Serif

Colors

Designer to choose colors to be used in the design.

Requirements
Must have
• Navigation: 1) Home 2) Auctions 3) Services 4) Real Estate 5 ) Previous Auctions 6) About Us 7) Contact Us

Sites referenced that client likes: https://www.gatherpledge.example/ and http://www.quillonbidhouse.example/ as examples of image rich sites. There will be large slideshow element and 4 calls to action (with any stock images suitable) 1) Real Estate 2) Auctions 3) Liquidations 4) Appraisals

Content will also include text (below) and auctions as seen at http://www.quillonbidhouse.example/ below the slideshow or as in the attached image.

Footer will have contact info, social icons (FB, Twitter, YT, RSS) and news posts widget

Colors will be that of the logo and any others to highlight/compliment the design.

Nice to have
• Use of dropdown menu styling

```html
<!DOCTYPE html>
<html lang="en">
<head>
<meta charset="utf-8">
<title>Brenwick Auctions</title>
<link href="https://fonts.googleapis.com/css2?family=Open+Sans:wght@400;600;700&family=Merriweather:wght@700&display=swap" rel="stylesheet">
<style>
:root{
  --navy:#14306b;
  --navy-dark:#0d2355;
  --blue:#1d4796;
  --blue-light:#2d5bb3;
  --red:#d42a20;
  --grey-bg:#eef0f3;
  --text:#333;
  --muted:#666;
  --white:#fff;
}
*{margin:0;padding:0;box-sizing:border-box}
html,body{width:781px;height:1200px;overflow:hidden}
body{font-family:"Open Sans",Arial,sans-serif;color:var(--text);background:var(--white);position:relative}
.wrap{position:absolute;left:100px;width:582px}

/* header */
.site-header{position:absolute;top:0;left:0;width:781px;height:100px;background:var(--white)}
.brand{position:absolute;left:100px;top:26px;display:flex;align-items:center;gap:8px}
.brand-mark{width:14px;height:14px;background:var(--navy)}
.brand-name{font-family:"Merriweather",Georgia,serif;font-weight:700;font-size:17px;color:var(--navy);letter-spacing:.5px;white-space:nowrap}
.top-contact{position:absolute;right:100px;top:14px;font-size:10px;color:var(--text)}
.lang{position:absolute;right:100px;top:36px;display:flex;align-items:center;gap:5px;font-size:9px;color:var(--muted)}
.lang-flag{width:16px;height:10px;background:linear-gradient(#2b3f8f,#c8324a)}
.main-nav{position:absolute;top:97px;left:0;width:781px;height:28px;background:var(--navy)}
.main-nav ul{list-style:none;display:flex;justify-content:flex-end;position:absolute;right:99px;top:0;height:28px}
.main-nav li{font-size:10px;font-weight:700;color:var(--white);padding:0 10px;line-height:28px}
.main-nav li.active{background:var(--blue-light)}

/* slider */
.hero{position:absolute;top:125px;left:0;width:781px;height:288px}
.hero-photo{position:absolute;inset:0;background:linear-gradient(100deg,#5a6a58 0%,#8a8f7c 30%,#c9c3b6 50%,#7a7463 75%,#4d5448 100%)}
.hero-caption{position:absolute;left:100px;top:90px;width:172px;padding:12px 12px 14px;background:rgba(20,30,50,.78);color:var(--white)}
.hero-caption h2{font-size:14px;font-weight:700;margin-bottom:8px;white-space:nowrap}
.hero-caption p{font-size:9.5px;line-height:1.45;margin-bottom:10px}
.btn-red{display:inline-block;background:var(--red);color:var(--white);font-size:9px;font-weight:700;padding:5px 10px}
.hero-dots{position:absolute;left:100px;top:268px;display:flex;gap:5px}
.hero-dots span{width:7px;height:7px;border-radius:50%;background:var(--white);opacity:.6}
.hero-dots span:first-child{opacity:1}
.hero-arrow{position:absolute;top:128px;width:26px;height:26px;border-radius:50%;background:rgba(255,255,255,.35)}
.hero-arrow svg{width:26px;height:26px}
.hero-arrow.prev{left:22px}.hero-arrow.next{right:22px}

/* calls to action */
.cta-band{position:absolute;top:413px;left:0;width:781px;height:48px;background:var(--navy-dark)}
.cta-row{top:438px;height:126px;display:flex;gap:14px}
.cta{position:relative;flex:1;border:3px solid var(--blue);background:var(--white);box-shadow:0 6px 8px rgba(0,0,0,.15)}
.cta-photo{position:absolute;inset:0}
.cta-tag{position:absolute;left:-3px;top:8px;background:var(--red);color:var(--white);font-size:8px;font-weight:700;padding:3px 6px}

/* main */
.content{position:absolute;top:592px;left:0;width:781px;height:470px;background:var(--grey-bg)}
.current{top:20px;width:372px}
.section-title{font-size:13px;font-weight:700;color:var(--navy);padding-bottom:6px;border-bottom:2px solid var(--blue);position:relative}
.section-title .pager{position:absolute;right:0;top:2px;width:16px;height:8px;background:var(--blue)}
.auction{display:flex;gap:10px;padding:14px 0;border-bottom:1px solid #d6d9de;height:132px}
.auction-thumb{width:78px;height:62px;flex:none;background:linear-gradient(#9fb6cf,#7b8a6e)}
.auction h3{font-size:9.5px;font-weight:700;color:var(--text);margin-bottom:4px}
.auction p{font-size:8px;line-height:1.5;color:var(--muted);margin-bottom:6px}
.auction .btn-red{font-size:7.5px;padding:4px 8px;margin-left:110px}
.auction .btn-plain{display:inline-block;font-size:7.5px;padding:4px 8px;background:var(--navy);color:var(--white)}

.sidebar{position:absolute;left:492px;top:20px;width:190px}
.widget{background:var(--white);box-shadow:0 3px 8px rgba(0,0,0,.15);margin-bottom:22px}
.widget-title{background:var(--navy);color:var(--white);font-size:12px;font-weight:600;text-align:center;padding:8px 0}
.widget-item{display:flex;gap:8px;padding:12px 10px;border-bottom:1px solid #e1e3e7}
.widget-item:last-child{border-bottom:0}
.widget-thumb{width:42px;height:36px;flex:none;background:linear-gradient(#9fb6cf,#7b8a6e)}
.widget-item h4{font-size:8.5px;font-weight:700;margin-bottom:3px}
.widget-item p{font-size:7px;line-height:1.45;color:var(--muted)}

/* footer */
.site-footer{position:absolute;top:1062px;left:0;width:781px;height:138px;background:var(--navy)}
.foot-brand{position:absolute;left:100px;top:20px;display:flex;align-items:center;gap:5px}
.foot-brand .brand-mark{background:var(--white);width:9px;height:9px}
.foot-brand .brand-name{color:var(--white);font-size:9.5px;letter-spacing:0}
.social{position:absolute;left:100px;top:72px;display:flex;gap:6px}
.social span{width:18px;height:18px;background:var(--blue-light)}
.copyright{position:absolute;left:100px;top:102px;font-size:7px;color:#c4cde0}
.foot-col{position:absolute;top:16px;color:var(--white)}
.foot-col h5{font-size:12px;font-weight:600;margin-bottom:8px}
.foot-col ul{list-style:none;font-size:8px;line-height:1.65;color:#dbe2f0}
.links{left:255px}
.links-2{left:320px;top:41px}
.older{left:430px;width:250px}
.post{margin-bottom:9px}
.post h6{font-size:8px;font-weight:700;display:flex;align-items:center;gap:5px;margin-bottom:2px}
.post h6 span{width:10px;height:7px;background:var(--red)}
.post p{font-size:7px;line-height:1.45;color:#c4cde0}
</style>
</head>
<body>

<header class="site-header">
  <div class="brand"><span class="brand-mark"></span><span class="brand-name">BRENWICK AUCTIONS</span></div>
  <div class="top-contact">(555) 014 2230 | info@brenwick.example</div>
  <div class="lang"><span class="lang-flag"></span>EN</div>
</header>

<nav class="main-nav">
  <ul>
    <li>Home</li><li>Auctions</li><li class="active">Services</li><li>Real Estate</li><li>Previous Auctions</li><li>About Us</li><li>Contact Us</li>
  </ul>
</nav>

<section class="hero">
  <div class="hero-photo" role="img" aria-label="Auction room with a quilt held up for bidders"></div>
  <div class="hero-caption">
    <h2>Lorem Ipsum Dolor</h2>
    <p>Lorem ipsum dolor sit amet, consectetur adipiscing elit, sed do eiusmod tempor incididunt ut</p>
    <span class="btn-red">Read More</span>
  </div>
  <div class="hero-dots"><span></span><span></span><span></span></div>
  <div class="hero-arrow prev"><svg viewBox="0 0 26 26"><path d="M15 8l-5 5 5 5" fill="none" stroke="#fff" stroke-width="2"/></svg></div>
  <div class="hero-arrow next"><svg viewBox="0 0 26 26"><path d="M11 8l5 5-5 5" fill="none" stroke="#fff" stroke-width="2"/></svg></div>
</section>

<div class="cta-band"></div>
<section class="wrap cta-row">
  <div class="cta"><div class="cta-photo" role="img" aria-label="House for sale" style="background:linear-gradient(#b9cde3,#8c9a82)"></div><span class="cta-tag">Real Estate</span></div>
  <div class="cta"><div class="cta-photo" role="img" aria-label="Auctioneer with bidding paddle" style="background:linear-gradient(#6d6a72,#a59a8d)"></div><span class="cta-tag">Auctions</span></div>
  <div class="cta"><div class="cta-photo" role="img" aria-label="Sale signs in a shop window" style="background:linear-gradient(#c23a35,#e7e2dc)"></div><span class="cta-tag">Liquidations</span></div>
  <div class="cta"><div class="cta-photo" role="img" aria-label="Real estate appraisal paperwork" style="background:linear-gradient(#e9e7e1,#b6b0a3)"></div><span class="cta-tag">Appraisals</span></div>
</section>

<main class="content">
  <section class="wrap current">
    <h2 class="section-title">CURRENT AUCTIONS<span class="pager"></span></h2>
    <article class="auction">
      <div class="auction-thumb" role="img" aria-label="Auction property"></div>
      <div>
        <h3>Lorem Ipsum Dolorsum</h3>
        <p>Lorem ipsum dolor sit amet, consectetur adipiscing elit, sed do eiusmod tempor incididunt ut labore et dolore magna aliqua. Ut enim ad minim veniam quis nostrud.</p>
        <span class="btn-plain">Details</span><span class="btn-red">Click to bid online</span>
      </div>
    </article>
    <article class="auction">
      <div class="auction-thumb" role="img" aria-label="Auction property"></div>
      <div>
        <h3>Lorem Ipsum Dolorsum</h3>
        <p>Lorem ipsum dolor sit amet, consectetur adipiscing elit, sed do eiusmod tempor incididunt ut labore et dolore magna aliqua. Ut enim ad minim veniam quis nostrud.</p>
        <span class="btn-plain">Details</span><span class="btn-red">Click to bid online</span>
      </div>
    </article>
    <article class="auction">
      <div class="auction-thumb" role="img" aria-label="Auction property"></div>
      <div>
        <h3>Lorem Ipsum Dolorsum</h3>
        <p>Lorem ipsum dolor sit amet, consectetur adipiscing elit, sed do eiusmod tempor incididunt ut labore et dolore magna aliqua. Ut enim ad minim veniam quis nostrud.</p>
        <span class="btn-plain">Details</span><span class="btn-red">Click to bid online</span>
      </div>
    </article>
  </section>

  <aside class="sidebar">
    <div class="widget">
      <h3 class="widget-title">Featured Auctions</h3>
      <div class="widget-item"><div class="widget-thumb" role="img" aria-label="Featured property"></div><div><h4>Lorem Ipsum Dolor</h4><p>Lorem ipsum dolor sit amet, consectetur adipiscing elit sed do.</p></div></div>
      <div class="widget-item"><div class="widget-thumb" role="img" aria-label="Featured property"></div><div><h4>Lorem Ipsum Dolor</h4><p>Lorem ipsum dolor sit amet, consectetur adipiscing elit sed do.</p></div></div>
    </div>
    <div class="widget">
      <h3 class="widget-title">Latest Posts</h3>
      <div class="widget-item"><div class="widget-thumb" role="img" aria-label="Post image"></div><div><h4>Lorem Ipsum Dolor</h4><p>Lorem ipsum dolor sit amet, consectetur adipiscing elit sed do.</p></div></div>
      <div class="widget-item"><div class="widget-thumb" role="img" aria-label="Post image"></div><div><h4>Lorem Ipsum Dolor</h4><p>Lorem ipsum dolor sit amet, consectetur adipiscing elit sed do.</p></div></div>
    </div>
  </aside>
</main>

<footer class="site-footer">
  <div class="foot-brand"><span class="brand-mark"></span><span class="brand-name">BRENWICK AUCTIONS</span></div>
  <div class="social"><span></span><span></span><span></span><span></span></div>
  <p class="copyright">Copyright@Brenwick2014, All Rights Reserved</p>
  <div class="foot-col links"><h5>Quick Links</h5><ul><li>Home</li><li>Auctions</li><li>Services</li><li>Real Estate</li></ul></div>
  <div class="foot-col links-2"><ul><li>Previous Auctions</li><li>About Us</li><li>Contact Us</li></ul></div>
  <div class="foot-col older"><h5>Older Posts</h5>
    <div class="post"><h6><span></span>Lorem Ipsum Dolorsum</h6><p>Lorem ipsum dolor sit amet, consectetur adipiscing elit, sed do eiusmod tempor incididunt.</p></div>
    <div class="post"><h6><span></span>Lorem Ipsum Dolorsum</h6><p>Lorem ipsum dolor sit amet, consectetur adipiscing elit, sed do eiusmod tempor incididunt.</p></div>
  </div>
</footer>

</body>
</html>
```